Startup fashion company needs high-end, stylish and hip business cards!

We need a business card design that uses a logo that we just completed with a ArtFolkHub artist.

Our company is Velmora. We work with fashion designers to display their designs on our website and handle all back-end fulfillment for them (fabric sourcing, garment manufacturing, customer service, etc.). The word Velmora is a play on fashion trunk shows, where designers will show their wares in a small, intimate setting. The final design should communicate high-end / luxe, chic, stylish, fashion-forward, hip!

We are using greys as our logo color (#2d2d2d, #ababab). We are also interested, for branding purposes and on our website, to use purple as a highlight color (#4a3455). I have the logo in other formats if needed.

Target Market(s)

Investors, customers, fashion designers, suppliers

Industry/Entity Type

Fashion

Contact Information for Business Card

There should be space for:
Name
Title
Address 1
Address 2
City, State Zip
USA
Phone
Email
Vocalo
Chirpline

If it makes sense to put one or more of the contact info on the same line, that is fine if it won't be confusing.

Font styles to use
Sans Serif
Other font styles liked:
• Would like the font to be complementary to our logo font/look and feel. The logo font is Caviar Dreams with a stylized 'N' according to the logo designer.

Colors
876aae
e4daea
f3f1f8
ffffff

Requirements
Must have
• The cards will most likely printed through PrintQuay and therefore must meet their upload file guidelines. There are also software templates for business cards that can be utilized. Information below from PrintQuay site.
• We support a variety of file formats for uploaded designs.
• Adobe Acrobat 9 Document (*.pdf) (recommended)
• Adobe Illustrator CS3 Artwork (*.ai) (recommended)
• Adobe Photoshop CS3 Image (*.psd) (recommended)
• Bitmap Image (*.bmp)
• GIF Image (*.gif)
• JPEG Image (*.jpg,*.jpeg)
• Microsoft PowerPoint 2010 Document (*.ppt)
• Microsoft Publisher 2010 Document (*.pub)
• Microsoft Word 2010 Document (*.doc)
• PCX Image (*.pcx)
• PICT Image (*.pic,*.pict,*.pct)
• PNG Image (*.png)
• PostScript Document (*.ps)
• TIFF Image (*.tif,*.tiff)
• Windows Enhanced Metafile (*.emf)
• Windows Metafile (*.wmf)
• The templates on their site:
• Using a downloadable template for your application will ensure that your dimensions, resolution and color settings match ours.
• - Adobe Photoshop (recommended) Download Horizontal Template
• - Adobe Illustrator (recommended) Download Horizontal Template
• If you are creating a PDF document in Acrobat Distiller, please use our Distiller settings.
• - Adobe Acrobat Distiller (recommended) Download Settings
• Sizing:
• Full Bleed Size
• 3.62" x 2.12"
• 92 x 54 mm
• 1085 x 635 pixels
• Document Trim Size
• 3.50" x 2.00"
• 89 x 51 mm
• 1050 x 600 pixels
Nice to have
• The back can use either the full logo or just the elephant or a combination? I'm imagining a full color backside...open to other suggestions!

```html
<!DOCTYPE html>
<html lang="en">
<head>
<meta charset="utf-8">
<title>Velmora Business Card</title>
<link rel="stylesheet" href="https://fonts.googleapis.com/css2?family=Quicksand:wght@400;500;700&display=swap">
<style>
  :root {
    --bg: #e9e9ec;
    --card: #ffffff;
    --ink: #2d2d2d;
    --grey: #ababab;
    --purple: #6f559c;
    --purple-deep: #3b2a66;
  }
  html, body {
    margin: 0;
    width: 1200px;
    height: 902px;
    overflow: hidden;
    background: var(--bg);
  }
  .card {
    position: absolute;
    left: 75px;
    top: 151px;
    width: 1050px;
    height: 600px;
    background: var(--card);
    overflow: hidden;
    font-family: "Quicksand", sans-serif;
    color: var(--ink);
    box-shadow: 0 6px 24px rgba(0,0,0,0.12);
  }
  .side-word {
    position: absolute;
    left: 34px;
    top: 0;
    height: 600px;
    writing-mode: vertical-rl;
    transform: rotate(180deg);
    font-size: 116px;
    font-weight: 400;
    line-height: 1;
    letter-spacing: 2px;
    color: var(--grey);
    text-align: center;
    white-space: nowrap;
  }
  .brand {
    position: absolute;
    right: 58px;
    top: 94px;
    display: flex;
    align-items: center;
    gap: 18px;
  }
  .brand-dot {
    width: 100px;
    height: 100px;
    border-radius: 50%;
    background: var(--purple-deep);
  }
  .brand-name {
    font-size: 108px;
    font-weight: 500;
    line-height: 1;
    letter-spacing: 4px;
    color: var(--ink);
  }
  .person {
    position: absolute;
    right: 58px;
    top: 258px;
    text-align: right;
  }
  .person-name {
    font-size: 46px;
    font-weight: 700;
    color: var(--purple);
    line-height: 1.1;
  }
  .person-title {
    font-size: 32px;
    font-weight: 500;
    line-height: 1.1;
  }
  .address {
    position: absolute;
    right: 554px;
    top: 426px;
    text-align: right;
    font-size: 25px;
    font-weight: 400;
    line-height: 30px;
  }
  .address .city { margin-bottom: 20px; }
  .contacts {
    position: absolute;
    right: 58px;
    top: 393px;
    margin: 0;
    padding: 0;
    list-style: none;
  }
  .contacts li {
    display: flex;
    justify-content: flex-end;
    align-items: center;
    gap: 22px;
    height: 41.5px;
    font-size: 25px;
    font-weight: 400;
  }
  .icon {
    width: 26px;
    height: 26px;
    background: var(--purple);
    display: block;
    flex: none;
  }
</style>
</head>
<body>
  <div class="card">
    <div class="side-word" aria-hidden="true">VELMORA</div>

    <div class="brand">
      <span class="brand-dot"></span>
      <span class="brand-name">VELMORA</span>
    </div>

    <div class="person">
      <div class="person-name">Employee Name</div>
      <div class="person-title">Managing Director</div>
    </div>

    <div class="address">
      <div class="city">City, State Zip USA</div>
      <div>Your Adress Inc 2nd Lane</div>
      <div>Ave Edison, NJ 00000</div>
    </div>

    <ul class="contacts">
      <li>0012 3456 789
        <svg class="icon" viewBox="0 0 26 26" aria-label="phone">
          <rect width="26" height="26" fill="#6f559c"/>
          <path d="M8 6 l3 0 1 4 -2 1.5 q1.5 3.5 4.5 4.5 l1.5 -2 4 1 0 3 q-1 1.5 -3 1.5 q-10 -1 -10.5 -11 q0 -2 1.5 -2.5z" fill="#fff"/>
        </svg>
      </li>
      <li>info@youremail.com
        <svg class="icon" viewBox="0 0 26 26" aria-label="email">
          <rect width="26" height="26" fill="#6f559c"/>
          <rect x="5" y="8" width="16" height="11" fill="none" stroke="#fff" stroke-width="1.6"/>
          <path d="M5 8 l8 6 8 -6" fill="none" stroke="#fff" stroke-width="1.6"/>
        </svg>
      </li>
      <li>Your Vocalo Address <span class="icon"></span></li>
      <li>Your Chirpline Address <span class="icon"></span></li>
    </ul>
  </div>
</body>
</html>
```